Personal logo & business cards
for owner of multiple businesses.
Hi qlindo,
I really like your design #16. Can you maybe try it in a couple different colour combinations, and maybe also with the 'MIRELA VOSK' part in a cursive text?
Thanks,
Mirela
Hello porvadesign:
I like the design on 19 & 20, but I'd prefer it without the logo on the front. Also, there's maybe too much purple... it's a bit too feminine. Can you try it with less purple or in another colour?
Thanks!
I don't currently have a logo or anything... and would prefer that there wasn't a logo for one of my businesses on the front of my card. A personal logo would be okay though.
@PH - Any logo to use? Thanks
Hey everyone,
Please make sure to read the brief a little more closely. I only want my name and personal contact information on the front of the card, and the names of the THREE businesses that I am involved in on the back of the card.
Thanks for your submissions!
Open to colour palette, but leaning more towards purple or green. No blues.

```html
<!DOCTYPE html>
<html lang="en">
<head>
<meta charset="utf-8">
<title>Mirela Vosk Trosdan – Business Cards</title>
<link rel="stylesheet" href="https://fonts.googleapis.com/css2?family=Arimo:wght@400;700&display=swap">
<style>
  :root {
    --page-bg: #eeeae4;
    --card-bg: #2b2b2d;
    --card-bg-light: #3a3a3c;
    --text: #f2f2f2;
    --text-soft: #d6d6d6;
    --purple: #8a2fb0;
    --purple-dark: #4e1670;
    --purple-light: #b056d6;
    --green: #48a83c;
    --green-dark: #23701f;
    --green-light: #78cc5e;
  }
  * { margin: 0; padding: 0; box-sizing: border-box; }
  html, body { width: 1200px; height: 901px; overflow: hidden; }
  body {
    background: var(--page-bg);
    font-family: "Arimo", Arial, sans-serif;
    position: relative;
  }
  .card {
    position: absolute;
    width: 452px;
    height: 266px;
    background: linear-gradient(160deg, var(--card-bg-light), var(--card-bg) 60%);
    overflow: hidden;
    box-shadow: 0 3px 8px rgba(0,0,0,.35);
    color: var(--text);
  }
  .card--purple { --accent: var(--purple); }
  .card--green  { --accent: var(--green); }
  .front-left  { left: 139px; top: 166px; }
  .front-right { left: 640px; top: 166px; }
  .back-left   { left: 139px; top: 450px; }
  .back-right  { left: 640px; top: 450px; }
  .swoosh { position: absolute; inset: 0; width: 100%; height: 100%; }
  .holder-name {
    position: absolute; left: 26px; top: 124px;
    font-weight: 700; font-size: 21px; letter-spacing: .2px;
  }
  .contact {
    position: absolute; left: 26px; top: 160px;
    font-size: 13.5px; line-height: 17px; color: var(--text-soft);
  }
  .contact-line { display: flex; align-items: center; gap: 5px; white-space: nowrap; }
  .contact-icon { width: 11px; height: 11px; flex: none; fill: var(--accent); }
  .ventures {
    position: absolute; left: 26px; top: 38px;
    font-size: 14px; line-height: 17px; color: var(--text-soft);
    list-style: none;
  }
  .ventures li + li { margin-top: 17px; }
  .website {
    position: absolute; right: 22px; bottom: 14px;
    font-size: 16px; color: var(--text);
  }
</style>
</head>
<body>

<svg width="0" height="0" style="position:absolute" aria-hidden="true">
  <defs>
    <linearGradient id="purpleFill" x1="0" y1="0" x2="1" y2="0">
      <stop offset="0" stop-color="#4e1670"/><stop offset=".5" stop-color="#b056d6"/><stop offset="1" stop-color="#8a2fb0"/>
    </linearGradient>
    <linearGradient id="greenFill" x1="0" y1="0" x2="1" y2="0">
      <stop offset="0" stop-color="#23701f"/><stop offset=".5" stop-color="#78cc5e"/><stop offset="1" stop-color="#48a83c"/>
    </linearGradient>
    <linearGradient id="silver" x1="0" y1="0" x2="1" y2="0">
      <stop offset="0" stop-color="#9a9a9a"/><stop offset=".45" stop-color="#f4f4f4"/><stop offset="1" stop-color="#b5b5b5"/>
    </linearGradient>
  </defs>
</svg>

<section class="card card--purple front-left">
  <svg class="swoosh" viewBox="0 0 452 266" aria-hidden="true">
    <path d="M0,0 H452 V28 C330,30 170,50 0,96 Z" fill="url(#purpleFill)"/>
    <path d="M0,104 C170,58 330,38 452,36" fill="none" stroke="url(#silver)" stroke-width="14"/>
    <path d="M0,118 C170,72 330,50 452,48" fill="none" stroke="#8a2fb0" stroke-width="2"/>
  </svg>
  <h1 class="holder-name">Mirela Vosk Trosdan</h1>
  <div class="contact">
    <div class="contact-line">212, 4830 3 Avenue NW Redmont, AB T4K 3R7</div>
    <div class="contact-line">
      <svg class="contact-icon" viewBox="0 0 12 12"><circle cx="6" cy="6" r="5.5"/></svg>555-218-4407
      <svg class="contact-icon" viewBox="0 0 12 12"><circle cx="6" cy="6" r="5.5"/></svg>555-641-9023
    </div>
    <div class="contact-line">
      <svg class="contact-icon" viewBox="0 0 12 12"><rect x="0.5" y="2" width="11" height="8"/><path d="M0.5,2 L6,7 L11.5,2" fill="none" stroke="#2b2b2d" stroke-width="1"/></svg>mirelatrosdan@mailbox.com
    </div>
  </div>
</section>

<section class="card card--green front-right">
  <svg class="swoosh" viewBox="0 0 452 266" aria-hidden="true">
    <path d="M0,0 H452 V28 C330,30 170,50 0,96 Z" fill="url(#greenFill)"/>
    <path d="M0,104 C170,58 330,38 452,36" fill="none" stroke="url(#silver)" stroke-width="14"/>
    <path d="M0,118 C170,72 330,50 452,48" fill="none" stroke="#48a83c" stroke-width="2"/>
  </svg>
  <h1 class="holder-name">Mirela Vosk Trosdan</h1>
  <div class="contact">
    <div class="contact-line">212, 4830 3 Avenue NW Redmont, AB T4K 3R7</div>
    <div class="contact-line">
      <svg class="contact-icon" viewBox="0 0 12 12"><circle cx="6" cy="6" r="5.5"/></svg>555-218-4407
      <svg class="contact-icon" viewBox="0 0 12 12"><circle cx="6" cy="6" r="5.5"/></svg>555-641-9023
    </div>
    <div class="contact-line">
      <svg class="contact-icon" viewBox="0 0 12 12"><rect x="0.5" y="2" width="11" height="8"/><path d="M0.5,2 L6,7 L11.5,2" fill="none" stroke="#2b2b2d" stroke-width="1"/></svg>mirelatrosdan@mailbox.com
    </div>
  </div>
</section>

<section class="card card--purple back-left">
  <svg class="swoosh" viewBox="0 0 452 266" aria-hidden="true">
    <path d="M452,100 C330,122 210,190 95,266 H452 Z" fill="url(#purpleFill)"/>
    <path d="M452,80 C320,104 180,176 50,266" fill="none" stroke="url(#silver)" stroke-width="16"/>
    <path d="M452,66 C320,90 170,160 30,266" fill="none" stroke="#8a2fb0" stroke-width="2"/>
  </svg>
  <ul class="ventures">
    <li>Mirela Vosk's Clearance Depot<br>- President.</li>
    <li>Bright Buys @ Tiny Prices<br>- President.</li>
    <li>Trosdan Group<br>- Partner.</li>
  </ul>
  <div class="website">www.mirelavosk.com</div>
</section>

<section class="card card--green back-right">
  <svg class="swoosh" viewBox="0 0 452 266" aria-hidden="true">
    <path d="M452,100 C330,122 210,190 95,266 H452 Z" fill="url(#greenFill)"/>
    <path d="M452,80 C320,104 180,176 50,266" fill="none" stroke="url(#silver)" stroke-width="16"/>
    <path d="M452,66 C320,90 170,160 30,266" fill="none" stroke="#48a83c" stroke-width="2"/>
  </svg>
  <ul class="ventures">
    <li>Mirela Vosk's Clearance Depot<br>- President.</li>
    <li>Bright Buys @ Tiny Prices<br>- President.</li>
    <li>Trosdan Group<br>- Partner.</li>
  </ul>
  <div class="website">www.mirelavosk.com</div>
</section>

</body>
</html>
```